Patient Satisfaction

We are extending our social listening and intelligence platform for Physicians to patient satisfaction app. Our platform monitors social media and review sites and collects, classifies and distilled patient satisfaction into nine Categories - Thoroughness, Answers Q's, Collaborative, Caring, Time Spent, Previous Success, Instruction Clarity, Follow-up and Reputation

The app will have three main states: (1) Home state showing the metric for each category, (2) a detailed page for each Category showing the metric, topics discussed and sites sourced, (3) Leaderboard showing Physicians with best scores.

If you follow our wireframes, please take liberty to extend it. We like the Panelo 6 tiles, but our wireframes fall far short of meeting its coolness and usefulness. For example, we don't have different size tiles, and would live them, or content on the tiles to make them more meaningful. [Note: use KV instead of GLH.]
Updates

The designs submitted to date look great, but they reminded me that my instructions were unclear. Feel free to follow the wireframes if you like the UI, but we also welcome your thoughts on UI in addition to look and feel. If you follow our wireframes, please take liberty to extend it. We like the Panelo 6 tile, but our wireframes falls far short of meeting its coolness and usefulness. For example, we don't have different size tiles or content on the tiles to make them more meaningful. If you've submitted designs, please feel free to revise them or submit a different look. And if you haven't submitted designs, please feel free to give us your best thoughts on UI and design.

Target Market(s)

US Physicians

Industry/Entity Type

Media

Font styles to use
Sans Serif

Colors
f37022
5c5c5c
33a6d7

Requirements
Must have
• Home state
Visual icons
Nice to have
• Leaderbaord

```html
<!DOCTYPE html>
<html lang="en">
<head>
<meta charset="utf-8">
<title>Dashboard</title>
<link rel="stylesheet" href="https://fonts.googleapis.com/css2?family=Roboto:wght@300;400;500;700;900&display=swap">
<style>
  :root {
    --page-bg: #eceef1;
    --orange-deep: #f37022;
    --orange-mid: #f79a24;
    --orange-light: #f9c12f;
    --stat-band: #f8ad3a;
    --stat-band-alt: #f9bb3a;
    --stat-text: #b8561a;
    --stat-value: #a9480f;
    --blue: #3aa6d8;
    --blue-dark: #2a93c8;
    --divider: rgba(255,255,255,0.28);
    --white: #ffffff;
    --grey: #5c5c5c;
  }
  * { box-sizing: border-box; margin: 0; padding: 0; }
  html, body {
    width: 1024px; height: 1200px; overflow: hidden;
    background: var(--page-bg);
    font-family: "Roboto", "Helvetica Neue", Arial, sans-serif;
  }
  .app-screen {
    position: absolute; left: 174px; top: 0;
    width: 676px; height: 1200px; overflow: hidden;
    background: var(--blue);
  }
  .hero {
    position: absolute; left: 0; top: 0; width: 676px; height: 556px;
    background: linear-gradient(160deg, var(--orange-light) 0%, var(--orange-mid) 55%, var(--orange-light) 100%);
  }
  .status-bar {
    position: absolute; top: 0; left: 0; right: 0; height: 54px;
    display: flex; align-items: center; justify-content: space-between;
    padding: 0 14px; color: var(--white); font-size: 23px; font-weight: 400;
  }
  .status-left, .status-right { display: flex; align-items: center; gap: 8px; width: 220px; }
  .status-right { justify-content: flex-end; }
  .signal { display: flex; gap: 3px; }
  .signal span { width: 9px; height: 9px; border-radius: 50%; background: var(--white); }
  .status-time { font-weight: 500; }
  .nav-bar {
    position: absolute; top: 60px; left: 0; right: 0; height: 70px;
    display: flex; align-items: center; justify-content: center;
  }
  .nav-title { color: var(--white); font-size: 40px; font-weight: 300; }
  .nav-menu { position: absolute; left: 2px; top: 22px; }
  .nav-share { position: absolute; right: 22px; top: 6px; }
  .score-ring {
    position: absolute; left: 162px; top: 174px; width: 350px; height: 350px;
    border-radius: 50%; background: rgba(243,112,34,0.18);
  }
  .score-circle {
    position: absolute; left: 174px; top: 186px; width: 326px; height: 326px;
    border-radius: 50%; background: var(--orange-deep); opacity: 0.92;
    display: flex; flex-direction: column; align-items: center; justify-content: center;
  }
  .score-value { color: var(--white); font-size: 156px; font-weight: 900; line-height: 1; letter-spacing: -4px; margin-top: 10px; }
  .score-unit { color: rgba(255,255,255,0.7); font-size: 48px; font-weight: 300; margin-top: 2px; }
  .stats-band {
    position: absolute; left: 0; top: 556px; width: 676px; height: 111px;
    display: flex; background: var(--stat-band);
  }
  .stat {
    flex: 1; display: flex; align-items: center; justify-content: center; gap: 14px;
    color: var(--stat-text); font-size: 29px; font-weight: 400;
  }
  .stat + .stat { border-left: 1px solid rgba(255,255,255,0.3); background: var(--stat-band-alt); }
  .stat b { color: var(--stat-value); font-weight: 700; }
  .tiles-large { position: absolute; left: 0; top: 667px; width: 676px; height: 307px; display: flex; }
  .tiles-small { position: absolute; left: 0; top: 974px; width: 676px; height: 226px; display: flex; border-top: 1px solid var(--divider); }
  .tile {
    flex: 1; display: flex; flex-direction: column; align-items: center; justify-content: flex-start;
    color: var(--white); font-weight: 700; font-size: 29px; line-height: 34px; background: var(--blue);
  }
  .tile + .tile { border-left: 1px solid var(--divider); }
  .tile--dark { background: var(--blue-dark); }
  .tile-icon { display: flex; align-items: center; justify-content: center; }
  .tiles-large .tile { padding-top: 54px; }
  .tiles-large .tile-icon { height: 152px; margin-bottom: 22px; }
  .tiles-small .tile { padding-top: 46px; }
  .tiles-small .tile-icon { height: 80px; margin-bottom: 30px; }
  .tile svg { fill: none; stroke: var(--white); stroke-width: 4; stroke-linejoin: round; stroke-linecap: round; }
  .tiles-small .tile svg { stroke-width: 3; }
</style>
</head>
<body>
<main class="app-screen">
  <section class="hero">
    <div class="status-bar">
      <div class="status-left">
        <div class="signal"><span></span><span></span><span></span><span></span><span></span></div>
        <span>Telvane</span>
        <svg width="26" height="20" viewBox="0 0 26 20"><path d="M2 7a16 16 0 0 1 22 0M6 11a10 10 0 0 1 14 0M10 15a4 4 0 0 1 6 0" stroke="#fff" stroke-width="2.6" fill="none" stroke-linecap="round"/><circle cx="13" cy="18" r="1.6" fill="#fff"/></svg>
      </div>
      <span class="status-time">9:23 AM</span>
      <div class="status-right">
        <svg width="18" height="18" viewBox="0 0 18 18"><path d="M17 1 1 8l7 2 2 7z" fill="#fff"/></svg>
        <span>66%</span>
        <svg width="48" height="22" viewBox="0 0 48 22"><rect x="1" y="2" width="41" height="18" rx="3" stroke="#fff" stroke-width="2" fill="none"/><rect x="4" y="5" width="24" height="12" fill="#fff"/><rect x="43" y="8" width="3" height="6" fill="#fff"/></svg>
      </div>
    </div>
    <div class="nav-bar">
      <svg class="nav-menu" width="36" height="22" viewBox="0 0 36 22"><path d="M2 3h32M2 11h32M2 19h32" stroke="#fff" stroke-width="3"/></svg>
      <h1 class="nav-title">Dashboard</h1>
      <svg class="nav-share" width="44" height="56" viewBox="0 0 44 56"><path d="M15 18H3v36h38V18H29M22 34V2M12 12 22 2l10 10" stroke="#fff" stroke-width="2.4" fill="none"/></svg>
    </div>
    <div class="score-ring"></div>
    <div class="score-circle">
      <span class="score-value">72</span>
      <span class="score-unit">KV</span>
    </div>
  </section>

  <section class="stats-band">
    <div class="stat">
      <svg width="54" height="50" viewBox="0 0 54 50" fill="none" stroke="#b8561a" stroke-width="2.4" stroke-linejoin="round"><path d="M2 2h32v20H16l-6 6v-6H2z"/><path d="M20 28v-6h14V12h18v24h-8v8l-8-8H20z"/></svg>
      <span>Comments: <b>22</b></span>
    </div>
    <div class="stat">
      <svg width="42" height="52" viewBox="0 0 42 52" fill="none" stroke="#b8561a" stroke-width="2.4" stroke-linejoin="round"><path d="M3 50V3M3 5h36l-6 10 6 10H3"/></svg>
      <span>Rank: <b>5/15</b></span>
    </div>
  </section>

  <section class="tiles-large">
    <div class="tile">
      <div class="tile-icon">
        <svg width="150" height="142" viewBox="0 0 150 142">
          <path d="M54 4h18v14h14v18H72v14H54V36H40V18h14z"/>
          <ellipse cx="96" cy="78" rx="22" ry="10"/>
          <path d="M4 50v88M4 120h142M146 52v86M4 96h54l8-12h62l8-14h10"/>
          <path d="M14 138v-12M136 138v-12"/>
        </svg>
      </div>
      <span>Bedside</span>
    </div>
    <div class="tile tile--dark">
      <div class="tile-icon">
        <svg width="146" height="150" viewBox="0 0 146 150">
          <circle cx="44" cy="66" r="18"/>
          <path d="M6 146v-22c0-18 14-30 38-30s38 12 38 30v22z"/>
          <path d="M100 4c24 0 42 12 42 28s-18 28-42 28c-4 0-8 0-11-1l-18 14 6-18c-12-5-19-13-19-23 0-16 18-28 42-28z"/>
        </svg>
      </div>
      <span>Communication</span>
    </div>
  </section>

  <section class="tiles-small">
    <div class="tile">
      <div class="tile-icon">
        <svg width="86" height="64" viewBox="0 0 86 64">
          <path d="M2 18 40 4l40 14-40 14z"/>
          <path d="M16 24v22c8 6 16 8 24 8s16-2 24-8V24"/>
          <path d="M72 22v22"/><circle cx="72" cy="50" r="5"/>
        </svg>
      </div>
      <span>Knowledge</span>
    </div>
    <div class="tile">
      <div class="tile-icon">
        <svg width="70" height="70" viewBox="0 0 70 70">
          <circle cx="35" cy="35" r="32"/><circle cx="35" cy="35" r="24"/>
          <path d="M35 20v15l-8 6M45 22l-10 13"/>
        </svg>
      </div>
      <span>Time Spent</span>
    </div>
    <div class="tile">
      <div class="tile-icon">
        <svg width="66" height="72" viewBox="0 0 66 72">
          <rect x="3" y="3" width="50" height="66" rx="3"/>
          <path d="M53 8h8v16h-8M53 28h8v16h-8M53 48h8v16h-8"/>
          <path d="M12 16h32M12 24h32M12 32h20"/>
          <path d="M22 42h8v6h6v8h-6v6h-8v-6h-6v-8h6z"/>
        </svg>
      </div>
      <span>Outcome</span>
    </div>
  </section>
</main>
</body>
</html>
```